Coffeeshop menu for filter tip

We want to have a cannabis (coffeeshop) menu in the size 25mm wide x 60mm wide. Some examples attached.

it must have the following text:
Menu

WEED p/g
Velotrine €16
Cinderfox €14
Tide Rambler €14
Marigolden €16
Grand Pelican €14
Copper Comet €14

HASH p/g
Baltic Ember €12
Harbor Velvet€11
Plum Rova €14
Dusk Maple €10

Target Market(s)

tourist in Amsterdam

Requirements
Nice to have
• cannabis sign leaf
• No Cigarettes allowed symbol

```html
<!DOCTYPE html>
<html lang="en">
<head>
<meta charset="utf-8">
<title>Amsterdam Coffeeshop Menu</title>
<link rel="stylesheet" href="https://fonts.googleapis.com/css2?family=Bebas+Neue&family=Bitter:wght@400;500&family=Kaushan+Script&family=Open+Sans:wght@400&display=swap">
<style>
  :root {
    --paper: #ffffff;
    --leaf-green: #2fb04a;
    --menu-red: #e8402e;
    --teal: #21a3a5;
    --ink: #1a1a1a;
  }
  * { margin: 0; padding: 0; box-sizing: border-box; }
  html, body { width: 1200px; height: 2876px; overflow: hidden; }
  body { background: var(--paper); }

  .menu-card {
    position: relative;
    width: 1200px;
    height: 2876px;
    overflow: hidden;
    background:
      radial-gradient(ellipse 560px 760px at 0% 100%, rgba(31,154,78,0.95), rgba(31,154,78,0) 70%),
      radial-gradient(ellipse 700px 460px at 100% 1450px, rgba(120,195,80,0.9), rgba(159,208,110,0) 70%),
      radial-gradient(ellipse 620px 520px at 700px 1900px, rgba(251,242,122,0.95), rgba(251,242,122,0) 70%),
      radial-gradient(ellipse 420px 520px at 0% 1150px, rgba(251,242,122,0.75), rgba(251,242,122,0) 70%),
      radial-gradient(ellipse 600px 400px at 800px 950px, rgba(200,228,236,0.8), rgba(228,241,242,0) 70%),
      linear-gradient(180deg, #ffffff 0%, #f7fbf6 25%, #eef6e2 55%, #e5f2d6 80%, #d6ecd0 100%);
  }

  .brand-title {
    position: absolute;
    left: 0; right: 0; top: 76px;
    text-align: center;
    font-family: "Bitter", serif;
    font-weight: 500;
    font-size: 80px;
    line-height: 1;
    color: var(--leaf-green);
  }

  .menu-heading {
    position: absolute;
    left: 0; right: 0; top: 178px;
    text-align: center;
    font-family: "Bebas Neue", sans-serif;
    font-weight: 400;
    font-size: 236px;
    line-height: 1;
    color: var(--menu-red);
    letter-spacing: 2px;
  }

  .section-title {
    position: absolute;
    font-family: "Kaushan Script", cursive;
    font-weight: 400;
    font-size: 150px;
    line-height: 1;
    color: var(--teal);
  }
  .section-title.weed { left: 276px; top: 460px; }
  .section-title.hash { left: 282px; top: 1350px; }

  .unit-label {
    position: absolute;
    left: 828px;
    font-family: "Bitter", serif;
    font-size: 56px;
    color: var(--ink);
  }
  .unit-label.weed { top: 518px; }
  .unit-label.hash { top: 1410px; }

  .price-list { position: absolute; left: 311px; width: 640px; list-style: none; }
  .price-list.weed { top: 645px; }
  .price-list.hash { top: 1520px; }
  .price-list li {
    display: flex;
    justify-content: space-between;
    align-items: center;
    height: 102.7px;
  }
  .item-name {
    font-family: "Bitter", serif;
    font-weight: 500;
    font-size: 56px;
    color: var(--ink);
    letter-spacing: 0.5px;
  }
  .item-price {
    width: 113px;
    font-family: "Open Sans", sans-serif;
    font-size: 48px;
    color: var(--ink);
    margin-top: -20px;
  }

  .leaf-placeholder {
    position: absolute;
    left: 176px; top: 1985px;
    width: 880px; height: 815px;
    background: radial-gradient(ellipse at 50% 45%, rgba(47,176,74,0.95), rgba(47,176,74,0.75) 45%, rgba(47,176,74,0) 72%);
  }

  .no-smoking {
    position: absolute;
    left: 384px; top: 1996px;
    display: flex;
    align-items: center;
    gap: 18px;
  }
  .no-smoking svg { width: 110px; height: 110px; }
  .no-smoking-label {
    font-family: "Open Sans", sans-serif;
    font-size: 48px;
    color: var(--ink);
    letter-spacing: 1px;
  }
</style>
</head>
<body>
  <main class="menu-card">
    <div class="brand-title">Amsterdam</div>
    <h1 class="menu-heading">MENU</h1>

    <h2 class="section-title weed">Weed</h2>
    <span class="unit-label weed">p/g</span>
    <ul class="price-list weed">
      <li><span class="item-name">Velotrine</span><span class="item-price">€16</span></li>
      <li><span class="item-name">Cinderfox</span><span class="item-price">€14</span></li>
      <li><span class="item-name">Tide Rambler</span><span class="item-price">€14</span></li>
      <li><span class="item-name">Marigolden</span><span class="item-price">€16</span></li>
      <li><span class="item-name">Grand Pelican</span><span class="item-price">€14</span></li>
      <li><span class="item-name">Copper Comet</span><span class="item-price">€14</span></li>
    </ul>

    <h2 class="section-title hash">Hash</h2>
    <span class="unit-label hash">p/g</span>
    <ul class="price-list hash">
      <li><span class="item-name">Baltic Ember</span><span class="item-price">€12</span></li>
      <li><span class="item-name">Harbor Velvet</span><span class="item-price">€11</span></li>
      <li><span class="item-name">Plum Rova</span><span class="item-price">€14</span></li>
      <li><span class="item-name">Dusk Maple</span><span class="item-price">€10</span></li>
    </ul>

    <div class="leaf-placeholder" role="img" aria-label="Large green cannabis leaf illustration"></div>

    <div class="no-smoking">
      <svg viewBox="0 0 100 100" aria-hidden="true">
        <circle cx="50" cy="50" r="44" fill="#ffffff" stroke="#e8402e" stroke-width="8"/>
        <rect x="20" y="52" width="52" height="10" fill="#1a1a1a"/>
        <rect x="72" y="52" width="8" height="10" fill="#1a1a1a"/>
        <path d="M30 46 q-4 -8 2 -14 q6 -6 2 -14" fill="none" stroke="#1a1a1a" stroke-width="3"/>
        <line x1="20" y1="20" x2="80" y2="80" stroke="#e8402e" stroke-width="8"/>
      </svg>
      <span class="no-smoking-label">NO CIGARETTES</span>
    </div>
  </main>
</body>
</html>
```